Design the 21st Golden Reel Indie Screen Week Poster. Think modern, chic, cool, film, movies - driving people to the film festival - the film festivla is in San Francisco and the SF East Bay. Our logo is attached. Dates will be determined soon . please use - November 2 - 11, 2018 (for placement) Keep in mind abstract, chic, modern - eye catching. website is www.grisw.example

Target Market(s)

25 - 45 year old - upper middle class

Industry/Entity Type

Film Production

Colors

Designer to choose colors to be used in the design.

Requirements
Must have
• logo (attached) www.grisw.example - chic modern design
Nice to have
• best coolest poster ever!
Should not have
• CLIP ART!!!

```html
<!DOCTYPE html>
<html lang="en">
<head>
<meta charset="utf-8">
<title>21st Golden Reel Indie Screen Week</title>
<link rel="stylesheet" href="https://fonts.googleapis.com/css2?family=Amatic+SC:wght@700&family=Poiret+One&display=swap">
<style>
  :root {
    --ink: #0b0b0b;
    --paper: #ffffff;
    --night: #030303;
    --sky: #3f8fe0;
    --violet: #5a3cc0;
    --indigo: #2b2a94;
    --magenta: #b8369a;
    --ember: #e82a48;
  }
  html, body {
    margin: 0;
    padding: 0;
    width: 849px;
    height: 1200px;
    overflow: hidden;
    background: var(--night);
  }
  .poster {
    position: relative;
    width: 849px;
    height: 1200px;
    overflow: hidden;
    background: var(--night);
  }
  .artwork-area {
    position: absolute;
    inset: 0;
    background:
      linear-gradient(90deg, rgba(3,3,3,0.75) 0%, rgba(3,3,3,0) 30%, rgba(3,3,3,0) 75%, rgba(3,3,3,0.6) 100%),
      linear-gradient(165deg, var(--sky) 0%, var(--violet) 35%, var(--indigo) 55%, var(--magenta) 78%, var(--ember) 100%);
  }
  .frame {
    position: absolute;
    left: 57px;
    top: 54px;
    width: 736px;
    height: 1104px;
    border: 4px solid var(--paper);
    box-sizing: border-box;
  }
  .panel {
    position: absolute;
    left: 152px;
    top: 264px;
    width: 542px;
    height: 723px;
    background: var(--paper);
  }
  .festival-name {
    margin: 0;
    font-family: "Amatic SC", "Comic Sans MS", cursive;
    font-weight: 700;
    color: var(--ink);
    text-transform: uppercase;
  }
  .edition {
    position: absolute;
    left: 246px;
    top: 112px;
    font-size: 230px;
    line-height: 1;
    letter-spacing: -6px;
  }
  .edition-suffix {
    position: absolute;
    left: 392px;
    top: 268px;
    font-size: 40px;
    line-height: 1;
    letter-spacing: 2px;
  }
  .title {
    position: absolute;
    left: 228px;
    top: 338px;
    font-size: 92px;
    line-height: 112px;
    letter-spacing: 5px;
  }
  .title span { display: block; }
  .name-mark {
    position: absolute;
    left: 196px;
    top: 384px;
    width: 16px;
    height: 16px;
    background: var(--ink);
  }
  .details {
    margin: 0;
    font-family: "Poiret One", "Century Gothic", sans-serif;
    color: var(--ink);
    text-transform: uppercase;
  }
  .dates {
    position: absolute;
    left: 248px;
    top: 718px;
    font-size: 33px;
  }
  .venues {
    position: absolute;
    left: 262px;
    top: 788px;
    font-size: 27px;
    line-height: 36px;
  }
  .website {
    position: absolute;
    left: 152px;
    width: 542px;
    top: 950px;
    text-align: center;
    font-size: 17px;
    font-weight: 400;
  }
</style>
</head>
<body>
<main class="poster">
  <div class="artwork-area" role="img" aria-label="Abstract flowing artwork in blue, violet, magenta and red tones"></div>

  <div class="frame"></div>
  <div class="panel"></div>

  <p class="festival-name edition">21</p>
  <p class="festival-name edition-suffix">st</p>

  <span class="name-mark"></span>
  <h1 class="festival-name title">
    <span>Golden Reel</span>
    <span>Indie Screen</span>
    <span>Week</span>
  </h1>

  <p class="details dates">November 2 - 11, 2018</p>
  <p class="details venues">SF East Bay<br>San Francisco</p>
  <p class="details website">www.grisw.example</p>
</main>
</body>
</html>
```